Corvane Solutions Website

Corvane Solutions (CS) provide Analytics & Enterprise Performance Management (EPM) advisory & consultancy services. We are passionate about data and making a difference for our clients by working in partnership with them, helping them on their journey to becoming an Corvane Solution. We deliver insights which give our clients a competitive edge and a much deeper understanding of their organisation.

We need a website which shows who we are, what we do and how we do it.

www.corvane-solutions.com is our very basic website at the moment. We want to completely revamp it with a corporate look

```html
<!DOCTYPE html>
<html lang="en">
<head>
<meta charset="utf-8">
<title>Corvane Solutions — Data Analytics &amp; EPM Consulting</title>
<link rel="stylesheet" href="https://fonts.googleapis.com/css2?family=Montserrat:wght@400;500;600;700&display=swap">
<style>
:root{
  --navy:#1d3b55;
  --navy-deep:#172b3d;
  --teal:#5ac3da;
  --teal-dark:#3aa9c4;
  --ink:#2a3b4c;
  --muted:#6f7d8a;
  --line:#e3e8ec;
  --white:#ffffff;
  --soft:#f4f6f8;
}
*{box-sizing:border-box;margin:0;padding:0}
html,body{width:1200px;height:4172px;overflow:hidden}
body{font-family:'Montserrat',sans-serif;color:var(--ink);background:var(--white);position:relative}
.abs{position:absolute}
.center{left:0;width:1200px;text-align:center}
.eyebrow{font-size:9px;letter-spacing:3px;color:var(--teal);font-weight:600;text-transform:uppercase}
.eyebrow::before,.eyebrow::after{content:"";display:inline-block;width:14px;height:1px;background:var(--teal);vertical-align:middle;margin:0 8px}
.title{font-size:27px;font-weight:600;color:var(--navy);letter-spacing:.5px;text-transform:uppercase}
.lead{font-size:10.5px;line-height:16px;color:var(--muted)}
.btn{display:inline-block;border-radius:14px;font-size:9px;font-weight:600;letter-spacing:1px;text-transform:uppercase;color:var(--white);background:var(--teal);padding:0 18px;height:24px;line-height:24px;white-space:nowrap}
.btn.navy{background:var(--navy)}

/* Hero */
.hero{top:0;left:0;width:1200px;height:590px;background:linear-gradient(180deg,#3b5670 0%,#5f7f98 45%,#8aa3b6 80%,#6e889d 100%)}
.hero-shade{top:0;left:0;width:1200px;height:590px;background:linear-gradient(180deg,rgba(18,34,50,.55),rgba(18,34,50,.15) 55%,rgba(18,34,50,.05))}
.brand{display:flex;align-items:center;gap:8px;color:var(--white);font-size:10px;font-weight:700;line-height:11px;letter-spacing:.5px}
.brand-dot{width:26px;height:26px;border-radius:50%;background:var(--white)}
.nav{top:32px;left:603px;display:flex;gap:19px;font-size:8.5px;font-weight:600;color:var(--white);letter-spacing:.5px;white-space:nowrap}
.nav .active{color:var(--teal);border-bottom:1px solid var(--teal);padding-bottom:3px}
.nav-sep{top:32px;left:866px;width:1px;height:10px;background:rgba(255,255,255,.5)}
.nav-phone{top:32px;left:885px;font-size:8.5px;font-weight:600;color:var(--white);display:flex;gap:5px;align-items:center;white-space:nowrap}
.nav-cta{top:26px;left:971px;width:99px;height:23px;line-height:23px;padding:0;text-align:center;font-size:8px}
.hero-eyebrow{top:218px}
.hero-title{top:238px;font-size:32px;line-height:38px;font-weight:600;color:var(--white);letter-spacing:.5px}
.hero-sub{top:321px;font-size:10.5px;color:var(--white)}
.hero-btn{top:357px;left:544px;width:112px;padding:0;text-align:center}
.scroll-chev{top:548px;left:592px}

/* Services */
.svc-eyebrow{top:655px}
.svc-title{top:676px}
.svc-lead{top:712px;left:365px;width:470px;text-align:center}
.card{top:802px;width:301px;height:401px}
.card-photo{position:absolute;inset:0}
.card-label{position:absolute;bottom:42px;width:100%;text-align:center;color:var(--white);font-size:10px;font-weight:700;letter-spacing:.8px}
.card-badge{position:absolute;bottom:-14px;left:127px;width:46px;height:46px;border-radius:50%;background:var(--white);display:flex;align-items:center;justify-content:center;box-shadow:0 2px 6px rgba(0,0,0,.12)}
.card-dark{background:linear-gradient(180deg,#1f3a52,#1a3247)}
.card-dark .inner{position:absolute;top:24px;left:24px;right:24px;text-align:center;color:var(--white)}
.card-mark{width:28px;height:28px;border-radius:50%;border:3px solid var(--white);margin:0 auto 12px}
.card-dark h3{font-size:15px;font-weight:700;letter-spacing:.5px;margin-bottom:9px}
.card-dark p{font-size:10px;line-height:15px}
.card-dark .btn{margin-top:14px;height:26px;line-height:26px}
.card-dark .mini{position:absolute;bottom:30px;left:135px;width:31px;height:31px;border-radius:50%;background:var(--teal);display:flex;align-items:center;justify-content:center}

/* Clients */
.clients-eyebrow{top:1295px}
.clients-eyebrow::before,.clients-eyebrow::after{display:none}
.clients-rule{top:1301px;height:1px;background:var(--line)}
.clients-band{top:1330px;left:0;width:1200px;height:173px;background:linear-gradient(180deg,#fff 0%,#fff 40%,#eef1f4 100%)}
.logo-row{top:1375px;left:130px;width:941px;height:60px;display:flex;align-items:center;justify-content:space-between;padding:0 30px}
.client{display:flex;align-items:center;gap:6px;font-size:12px;font-weight:600;color:#7b8792;white-space:nowrap}
.client i{display:block;width:14px;height:14px;border-radius:50%;background:#aab3bb}
.client.lit{background:var(--white);box-shadow:0 3px 14px rgba(0,0,0,.12);width:165px;height:62px;justify-content:center;color:var(--navy);font-size:14px}
.arrow{top:1393px;color:#b7c0c8;font-size:18px}

/* Testimonials */
.testi{top:1503px;left:0;width:1200px;height:415px;background:linear-gradient(90deg,#26323d 0%,#5b6670 40%,#3d4752 70%,#1f2a35 100%)}
.testi-shade{top:1503px;left:0;width:1200px;height:415px;background:rgba(20,30,40,.45)}
.testi-eyebrow{top:1570px}
.testi-title{top:1590px;color:var(--white);font-size:25px}
.testi-avatar{top:1664px;left:573px;width:54px;height:54px;border-radius:50%;background:linear-gradient(180deg,#d8d2cc,#b9b0a8);border:3px solid var(--white)}
.quote{top:1735px;left:265px;width:670px;text-align:center;color:var(--white);font-size:13px;line-height:19px}
.stars{top:1797px;color:var(--teal);font-size:11px;letter-spacing:3px}
.who{top:1824px;color:var(--white);font-size:10px;line-height:15px}
.who b{font-weight:700}

/* About */
.about-img{top:1980px;left:130px;width:460px;height:288px;background:linear-gradient(135deg,#d8d9d6 0%,#a9b0b3 40%,#717a7f 75%,#c4c6c2 100%)}
.dots{top:2252px;left:345px;display:flex;gap:5px}
.dots span{width:6px;height:6px;border-radius:50%;border:1px solid var(--white)}
.dots span.on{background:var(--white)}
.about-eyebrow{top:1982px;left:648px;font-size:8px;letter-spacing:2.5px;color:var(--teal);font-weight:600}
.about-title{top:2001px;left:647px;font-size:25px;font-weight:600;color:var(--navy)}
.about-text{top:2040px;left:648px;width:340px;font-size:10px;line-height:15px;color:var(--muted)}
.about-text p+p{margin-top:9px}
.about-rule{top:2183px;left:648px;width:343px;height:1px;background:var(--line)}
.about-call{top:2193px;left:648px;font-size:10px;color:var(--muted)}
.about-btns{top:2220px;left:647px;display:flex;gap:12px}
.about-btns .btn{height:26px;line-height:26px;padding:0 18px}

/* Values */
.values-rule{top:2331px;height:1px;background:var(--line)}
.values-eyebrow{top:2325px}
.values-eyebrow::before,.values-eyebrow::after{display:none}
.value{top:2393px;width:220px;text-align:center}
.value-icon{position:relative;width:64px;height:64px;border-radius:50%;background:var(--navy);margin:0 auto;display:flex;align-items:center;justify-content:center}
.value-icon .tag{position:absolute;bottom:-8px;left:24px;width:16px;height:16px;border-radius:50%;background:var(--teal);border:2px solid var(--white)}
.value-icon.ring{background:var(--navy);border:4px solid var(--teal);box-shadow:inset 0 0 0 3px var(--white)}
.value-icon.ring span{color:var(--white);font-size:19px;font-weight:600}
.value h4{margin-top:24px;font-size:10.5px;font-weight:700;color:var(--navy)}
.value.hl h4{color:var(--teal);margin-top:14px}
.value p{margin-top:8px;font-size:10px;line-height:14px;color:var(--muted)}

/* Team */
.team{top:2602px;left:0;width:1200px;height:544px;background:linear-gradient(180deg,#e8ecef 0%,#f7f8fa 40%,#ffffff 100%)}
.team-eyebrow{top:2667px}
.team-title{top:2688px}
.team-lead{top:2724px;left:370px;width:460px;text-align:center}
.filters{top:2816px;left:0;width:1200px;display:flex;justify-content:center;gap:4px}
.filters .btn{height:24px;line-height:24px;background:var(--navy);font-size:8.5px;padding:0 18px}
.filters .btn.on{background:var(--teal);padding:0 26px}
.member{top:2886px;width:190px;text-align:center}
.member .face{width:124px;height:124px;border-radius:50%;margin:0 auto;border:5px solid var(--white);box-shadow:0 3px 10px rgba(0,0,0,.15)}
.member h5{margin-top:20px;font-size:9.5px;font-weight:700;color:var(--navy)}
.member p{margin-top:4px;font-size:9px;line-height:13px;color:var(--muted)}
.member.on h5{color:var(--teal)}
.bio{position:absolute;top:76px;left:77px;width:36px;height:12px;border-radius:6px;background:var(--navy-deep);color:var(--white);font-size:6.5px;line-height:12px}
.bio-dot{position:absolute;top:48px;left:86px;width:18px;height:18px;border-radius:50%;background:var(--white)}

/* Contact band */
.cta{top:3146px;left:0;width:1200px;height:305px;background:linear-gradient(135deg,#2a3643 0%,#55626e 45%,#34414d 70%,#1b2631 100%)}
.cta-shade{top:3146px;left:0;width:1200px;height:305px;background:rgba(15,25,35,.35)}
.cta-eyebrow{top:3210px}
.cta-title{top:3230px;color:var(--white);font-size:26px;line-height:32px;font-weight:600}
.cta-text{top:3299px;left:370px;width:460px;text-align:center;color:var(--white);font-size:10px;line-height:15px}
.cta-btn{top:3356px;left:542px;width:116px;padding:0;text-align:center;height:26px;line-height:26px}

/* Reach */
.reach-eyebrow{top:3514px}
.reach-title{top:3535px}
.reach-lead{top:3573px}
.reach{top:3632px;width:260px;text-align:center}
.reach-icon{width:62px;height:62px;border-radius:50%;background:var(--navy);margin:0 auto;display:flex;align-items:center;justify-content:center}
.reach-icon.teal{background:var(--teal)}
.reach h6{margin-top:17px;font-size:10.5px;font-weight:700;color:var(--navy)}
.reach.hl h6{color:var(--teal)}
.reach p{margin-top:7px;font-size:10px;line-height:15px;color:var(--muted)}
.reach p.link{color:var(--teal)}

/* Map + footer */
.map{top:3843px;left:0;width:1200px;height:121px;background:linear-gradient(90deg,#8fd6e6 0%,#5ec3da 50%,#3db0cc 100%)}
.map-pin{top:3891px;left:584px;width:32px;height:32px;border-radius:50%;border:2px solid var(--white)}
.footer{top:3964px;left:0;width:1200px;height:208px;background:var(--navy-deep)}
.foot-brand{top:4014px;left:532px}
.foot-brand .brand-dot{width:32px;height:32px}
.foot-brand span{font-size:12px;line-height:13px}
.copy{top:4060px;font-size:8px;letter-spacing:.5px;color:#8a99a7}
.foot-links{top:4077px;font-size:8px;font-weight:600;letter-spacing:.5px;color:var(--white);display:flex;justify-content:center;gap:16px}
.social{top:4106px;left:0;width:1200px;display:flex;justify-content:center;gap:10px}
.social span{width:20px;height:20px;border-radius:50%;background:var(--teal)}
.social span.plain{background:transparent;border:1px solid #8a99a7;width:14px;height:14px;margin-top:3px}
</style>
</head>
<body>

<!-- Hero -->
<section class="abs hero" role="img" aria-label="Looking up at glass skyscrapers against a blue sky"></section>
<div class="abs hero-shade"></div>
<div class="abs brand" style="top:24px;left:130px"><span class="brand-dot"></span><span>CORVANE<br>SOLUTIONS</span></div>
<nav class="abs nav"><span class="active">HOME</span><span>SERVICES</span><span>ABOUT</span><span>TEAM</span><span>CONTACT</span></nav>
<span class="abs nav-sep"></span>
<div class="abs nav-phone">
  <svg width="9" height="9" viewBox="0 0 24 24" fill="none" stroke="#fff" stroke-width="2.4"><path d="M5 3h4l2 5-3 2a12 12 0 0 0 6 6l2-3 5 2v4a2 2 0 0 1-2 2A18 18 0 0 1 3 5a2 2 0 0 1 2-2z"/></svg>01 555 0142</div>
<span class="abs btn nav-cta">&#10148; GET STARTED</span>
<div class="abs center eyebrow hero-eyebrow">Advise &amp; Architect</div>
<h1 class="abs center hero-title">DATA ANALYTICS &amp;<br>EPM CONSULTING SERVICES</h1>
<p class="abs center hero-sub">Transforming organisations by unlocking your most valuable asset - your data.</p>
<span class="abs btn hero-btn">EXPLORE MORE</span>
<svg class="abs scroll-chev" width="16" height="10" viewBox="0 0 16 10" fill="none" stroke="#fff" stroke-width="1.4"><path d="M4 3l4 4 4-4"/></svg>

<!-- Services -->
<div class="abs center eyebrow svc-eyebrow">Services</div>
<h2 class="abs center title svc-title">What We Do</h2>
<p class="abs lead svc-lead">CS are a Data Analytics &amp; EPM company, specialising in the implementation and support of Business Intelligence, EPM and Data Analytics business solutions, both in the Cloud and on-premise.</p>

<div class="abs card" style="left:130px">
  <div class="card-photo" role="img" aria-label="Hands typing on a laptop showing analytics dashboards" style="background:linear-gradient(160deg,#c9cdd0 0%,#9aa2a8 45%,#6d777f 100%)"></div>
  <div class="card-label">ADVISE &amp; ARCHITECT</div>
  <div class="card-badge"><svg width="16" height="14" viewBox="0 0 24 22" fill="none" stroke="#1d3b55" stroke-width="2"><rect x="2" y="2" width="20" height="13" rx="1"/><path d="M8 20h8M12 15v5"/></svg></div>
</div>

<div class="abs card card-dark" style="left:450px">
  <div class="inner">
    <div class="card-mark"></div>
    <h3>DESIGN &amp; IMPLEMENT</h3>
    <p>Working with the project management team, through each stage of the project, with clearly defined deliverables and well exercised plans to deliver them.</p>
    <span class="btn">LEARN MORE</span>
  </div>
  <div class="mini"><svg width="13" height="13" viewBox="0 0 24 24" fill="none" stroke="#fff" stroke-width="2"><rect x="3" y="3" width="18" height="18" rx="2"/><path d="M8 16V9M12 16v-5M16 16v-3"/></svg></div>
</div>

<div class="abs card" style="left:769px">
  <div class="card-photo" role="img" aria-label="Businessman holding a tablet with floating financial figures" style="background:linear-gradient(160deg,#2c4a66 0%,#5f84a3 45%,#b5c8d6 100%)"></div>
  <div class="card-label">OPTIMISE &amp; MANAGE</div>
  <div class="card-badge"><svg width="16" height="14" viewBox="0 0 24 22" fill="none" stroke="#1d3b55" stroke-width="2"><path d="M2 20h20M4 16l5-6 4 4 7-8"/></svg></div>
</div>

<!-- Clients -->
<div class="abs clients-rule" style="left:0;width:555px"></div>
<div class="abs clients-rule" style="left:645px;width:555px"></div>
<div class="abs center eyebrow clients-eyebrow">Clients</div>
<div class="abs clients-band"></div>
<span class="abs arrow" style="left:128px">&#8249;</span>
<span class="abs arrow" style="left:1060px">&#8250;</span>
<div class="abs logo-row">
  <span class="client"><i></i>Linkwise</span>
  <span class="client">Echofield</span>
  <span class="client lit">NEXORA LAB</span>
  <span class="client" style="font-size:9px"><i></i>Meridian Law</span>
  <span class="client"><i style="border-radius:2px"></i>BOLTRIX</span>
</div>

<!-- Testimonials -->
<section class="abs testi" role="img" aria-label="Business professionals in an office with laptops and trading charts"></section>
<div class="abs testi-shade"></div>
<div class="abs center eyebrow testi-eyebrow">Testimonials</div>
<h2 class="abs center title testi-title">What Our Clients Say</h2>
<div class="abs testi-avatar" role="img" aria-label="Client portrait"></div>
<span class="abs arrow" style="top:1748px;left:210px;color:rgba(255,255,255,.6)">&#8249;</span>
<p class="abs quote">“Lorem Ipsum is simply dummy text of the printing and typesetting industry. Lorem Ipsum has been the industry's standard dummy text ever since the 1500s, when an unknown printer took a galley of type and scrambled it to make a type specimen book.”</p>
<div class="abs center stars">&#9734;&#9734;&#9734;&#9734;&#9734;</div>
<div class="abs center who"><b>Tomas</b><br>Harwick</div>

<!-- About -->
<div class="abs about-img" role="img" aria-label="Team meeting around a table with a laptop, tablet and printed reports"></div>
<div class="abs dots"><span class="on"></span><span></span><span></span></div>
<div class="abs about-eyebrow">ABOUT</div>
<h2 class="abs about-title">Who We Are</h2>
<div class="abs about-text">
  <p>Corvane Solutions is an exciting start-up in the Data Analytics and EPM space. Founded in 2019, CS specialise in the implementation and support of BI, EPM and Data Analytics business solutions, both in the Cloud and on-premise.</p>
  <p>We work with our clients to help them on their journey to becoming an Corvane Solution by leveraging their most valuable asset, their data and helping them to gain a competitive advantage over their competitors.</p>
</div>
<div class="abs about-rule"></div>
<div class="abs about-call">Call us or email us for more information</div>
<div class="abs about-btns">
  <span class="btn">&#9990; 01 555 0142</span>
  <span class="btn navy">&#9993; EMAIL US</span>
</div>

<!-- Values -->
<div class="abs values-rule" style="left:0;width:555px"></div>
<div class="abs values-rule" style="left:645px;width:555px"></div>
<div class="abs center eyebrow values-eyebrow">Values</div>

<div class="abs value" style="left:130px">
  <div class="value-icon"><svg width="26" height="26" viewBox="0 0 24 24" fill="none" stroke="#fff" stroke-width="1.5"><rect x="3" y="3" width="18" height="13"/><path d="M7 12l3-3 3 2 4-4M8 20l4-4 4 4"/></svg><span class="tag"></span></div>
  <h4>Stategy</h4>
  <p>Lorem Ipsum is simply dummy text of the printing and typesetting industry. Lorem Ipsum has been</p>
</div>
<div class="abs value hl" style="left:370px">
  <div class="value-icon ring"><span>02</span></div>
  <h4>Approach</h4>
  <p>Lorem Ipsum is simply dummy text of the printing and typesetting industry. Lorem Ipsum has been</p>
</div>
<div class="abs value" style="left:609px">
  <div class="value-icon"><svg width="26" height="26" viewBox="0 0 24 24" fill="none" stroke="#fff" stroke-width="1.5"><circle cx="12" cy="12" r="9"/><circle cx="12" cy="12" r="5"/><circle cx="12" cy="12" r="1.5"/></svg><span class="tag"></span></div>
  <h4>Vision</h4>
  <p>Lorem Ipsum is simply dummy text of the printing and typesetting industry. Lorem Ipsum has been</p>
</div>
<div class="abs value" style="left:849px">
  <div class="value-icon"><svg width="26" height="26" viewBox="0 0 24 24" fill="none" stroke="#fff" stroke-width="1.5"><path d="M4 20h16M7 20l5-14 5 14M12 6V3l4 1-4 1"/></svg><span class="tag"></span></div>
  <h4>Mission</h4>
  <p>Lorem Ipsum is simply dummy text of the printing and typesetting industry. Lorem Ipsum has been</p>
</div>

<!-- Team -->
<section class="abs team" role="img" aria-label="Soft light grey architectural background"></section>
<div class="abs center eyebrow team-eyebrow">Team</div>
<h2 class="abs center title team-title">Our People</h2>
<p class="abs lead team-lead">We work with our clients to help them on their journey to becoming an Corvane Solution by leveraging their most valuable asset, their data and helping them to gain a competitive advantage over their competitors.</p>
<div class="abs filters"><span class="btn">ALL</span><span class="btn on">MANAGEMENT</span><span class="btn">ANALYTICS</span><span class="btn">CONSULTANTS</span></div>

<div class="abs member" style="left:129px">
  <div class="face" role="img" aria-label="Team member portrait" style="background:linear-gradient(180deg,#e9e6e2,#b7a596)"></div>
  <h5>CS MEMBER NAME</h5><p>Service Delivery Manager at<br>Corvane Solutions</p>
</div>
<div class="abs member" style="left:315px">
  <div class="face" role="img" aria-label="Team member portrait" style="background:linear-gradient(180deg,#eeeeee,#8e8d8f)"></div>
  <h5>CS MEMBER NAME</h5><p>EPM Consultant</p>
</div>
<div class="abs member on" style="left:503px">
  <div class="face" role="img" aria-label="Team member portrait with teal overlay" style="background:linear-gradient(180deg,#7fd1e3,#3aa9c4)"></div>
  <span class="bio-dot"></span><span class="bio">View Bio</span>
  <h5>CS MEMBER NAME</h5><p>CTO at Corvane Solutions</p>
</div>
<div class="abs member" style="left:691px">
  <div class="face" role="img" aria-label="Team member portrait" style="background:linear-gradient(180deg,#f0eeec,#9a7b62)"></div>
  <h5>CS MEMBER NAME</h5><p>Data Analytics Consultant @<br>Corvane Solutions</p>
</div>
<div class="abs member" style="left:877px">
  <div class="face" role="img" aria-label="Team member portrait" style="background:linear-gradient(180deg,#d98d86,#a85048)"></div>
  <h5>CS MEMBER NAME</h5><p>President at Corvane Solutions,<br>LLC</p>
</div>

<!-- Contact band -->
<section class="abs cta" role="img" aria-label="Dark view of city skyscrapers from below"></section>
<div class="abs cta-shade"></div>
<div class="abs center eyebrow cta-eyebrow">Support</div>
<h2 class="abs center cta-title">CONTACT US TO DISCUSS YOUR<br>BUSINESS NEEDS</h2>
<p class="abs cta-text">Corvane Solutions (CS) is an EPM and Analytics consultancy who are passionate about data and making a difference for our clients.</p>
<span class="abs btn cta-btn">&#9993; CONTACT US</span>

<!-- How to reach us -->
<div class="abs center eyebrow reach-eyebrow">Contact</div>
<h2 class="abs center title reach-title">How To Reach Us</h2>
<p class="abs center lead reach-lead">Lorem Ipsum is simply dummy text of the printing and typesetting industry.</p>

<div class="abs reach" style="left:150px">
  <div class="reach-icon"><svg width="24" height="24" viewBox="0 0 24 24" fill="none" stroke="#fff" stroke-width="1.6"><path d="M5 3h4l2 5-3 2a12 12 0 0 0 6 6l2-3 5 2v4a2 2 0 0 1-2 2A18 18 0 0 1 3 5a2 2 0 0 1 2-2z"/></svg></div>
  <h6>Phone</h6><p class="link">01 555 0142</p>
</div>
<div class="abs reach hl" style="left:469px">
  <div class="reach-icon teal"><svg width="24" height="24" viewBox="0 0 24 24" fill="none" stroke="#fff" stroke-width="1.6"><path d="M12 21s-6-6-6-11a6 6 0 0 1 12 0c0 5-6 11-6 11z"/><circle cx="12" cy="10" r="2.2"/></svg></div>
  <h6>Address</h6><p>14 Harbour View Road, Ringsend,<br>Dublin 4, D04 XY12</p>
</div>
<div class="abs reach" style="left:790px">
  <div class="reach-icon"><svg width="24" height="24" viewBox="0 0 24 24" fill="none" stroke="#fff" stroke-width="1.6"><rect x="3" y="5" width="18" height="14" rx="1"/><path d="M3 6l9 7 9-7"/></svg></div>
  <h6>Email</h6><p class="link">info@corvane-solutions.com</p>
</div>

<!-- Map + footer -->
<section class="abs map" role="img" aria-label="Street map of the office location tinted in teal"></section>
<div class="abs map-pin"></div>
<footer class="abs footer"></footer>
<div class="abs brand foot-brand"><span class="brand-dot"></span><span>CORVANE<br>SOLUTIONS</span></div>
<p class="abs center copy">© 2022 CORVANE SOLUTIONS, LLC. ALL RIGHTS RESERVED</p>
<div class="abs center foot-links"><span>PRIVACY POLICY</span><span>TERMS &amp; CONDITIONS</span></div>
<div class="abs social"><span></span><span class="plain"></span></div>

</body>
</html>
```